Business Card Design Project

I am community manager and social media strategist. I need a double sided business card with company logo and name. Looking for something professional, elegant but also a little bit original.

Industry/Entity Type

Business

Requirements
Must have
• - The logo and the colours are the company colours and a required to stay.
- The size should be: 84 x 55 mm (or 3.30 x 2.16)
- The file size should be: 1039 x 697 pixels (300 dpi)
- I'd like rounded corners. :)

Use the following contact information for the card:

Lucile Bravant
Stratégie médias sociaux / community management / édition de sites sociaux
mob. : 0687152930
lucile.bravant@maivox.fr
Twitter. : @lbravant
Skype : bravant.lucile

```html
<!DOCTYPE html>
<html lang="fr">
<head>
<meta charset="utf-8">
<title>Lucile Bravant – Carte de visite</title>
<link rel="stylesheet" href="https://fonts.googleapis.com/css2?family=Barlow:wght@400;500;600&display=swap">
<style>
  :root {
    --page-bg: #ffffff;
    --card-light: #ffffff;
    --card-dark: #0d5689;
    --ink-blue: #1d5b8c;
    --ink-white: #ffffff;
    --ink-soft: #d6e3f0;
    --deco-light: #e3eaf3;
    --deco-dark: #3a6f9c;
    --accent: #2a8fd0;
  }
  * { margin: 0; padding: 0; box-sizing: border-box; }
  html, body {
    width: 1200px; height: 900px; overflow: hidden;
    background: var(--page-bg);
    font-family: "Barlow", "Helvetica Neue", Arial, sans-serif;
  }
  .canvas { position: relative; width: 1200px; height: 900px; }
  .card {
    position: absolute; top: 285px;
    width: 503px; height: 328px;
    border-radius: 42px; overflow: hidden;
  }
  .card--front { left: 60px; background: var(--card-light); box-shadow: 0 0 0 1px #eef1f5; }
  .card--back { left: 637px; background: var(--card-dark); }
  .card__deco {
    position: absolute; left: -90px; top: -40px;
    width: 330px; height: 330px; border-radius: 50%;
  }
  .card--front .card__deco { background: var(--deco-light); opacity: .7; }
  .card--back .card__deco { background: var(--deco-dark); opacity: .55; }
  .brand {
    position: absolute; right: 34px; top: 30px;
    display: flex; flex-direction: column; align-items: flex-end; gap: 10px;
  }
  .brand__dot { width: 72px; height: 72px; border-radius: 50%; background: var(--accent); margin-right: 28px; }
  .brand__name {
    font-weight: 600; font-size: 34px; letter-spacing: 1px;
    color: var(--ink-blue); line-height: 1;
  }
  .identity {
    position: absolute; right: 34px; top: 198px; text-align: right;
    color: var(--ink-blue);
  }
  .identity__name { font-size: 27px; font-weight: 400; line-height: 1.2; margin-bottom: 8px; }
  .identity__role { font-size: 16px; line-height: 21px; }
  .contact {
    position: absolute; right: 32px; top: 254px; text-align: right;
    color: var(--ink-soft); font-size: 16px; line-height: 21px;
  }
  .contact__label { color: var(--ink-white); font-weight: 500; }
</style>
</head>
<body>
<main class="canvas">
  <section class="card card--front" aria-label="Recto">
    <div class="card__deco" aria-hidden="true"></div>
    <div class="brand">
      <span class="brand__dot" aria-hidden="true"></span>
      <span class="brand__name">NOVELIA</span>
    </div>
    <div class="identity">
      <p class="identity__name">Lucile Bravant</p>
      <p class="identity__role">Stratégie médias sociaux</p>
      <p class="identity__role">Community management</p>
      <p class="identity__role">Édition de sites sociaux</p>
    </div>
  </section>

  <section class="card card--back" aria-label="Verso">
    <div class="card__deco" aria-hidden="true"></div>
    <div class="contact">
      <p><span class="contact__label">mob.</span> 0687152930 | lucile.bravant@maivox.fr</p>
      <p><span class="contact__label">Twitter</span> @lbravant | <span class="contact__label">Skype</span> bravant.lucile</p>
    </div>
  </section>
</main>
</body>
</html>
```